Business Card Design Project

Looking for a simple and stylish business card. We are an Advertising Company. The card Must feature the company logo (attached) and also this info.
p: 0461528390
e: sales@jh-promo.com.au
w: www.jh-promo.com.au
We Advertise mainly using TV screens featured in restaurants and cafe. See website for more about the business.
Not really looking for a plain background, but at the same time do not want to much happening in the Background. I am not really to fussy though with the design or the colour scheme, and I am leaving the creativity part up to you creative designers.
Business

```html
<!DOCTYPE html>
<html lang="en">
<head>
<meta charset="utf-8">
<title>JH PROMO Business Card</title>
<link rel="stylesheet" href="https://fonts.googleapis.com/css2?family=Jost:wght@300;400;600&display=swap">
<style>
  :root {
    --backdrop: #b9b9b9;
    --card: #ffffff;
    --pink: #e4195a;
    --pink-light: #f47aa0;
    --plum: #5a1030;
    --blue: #2a5aa8;
    --blue-dark: #0f2660;
    --blue-light: #a8c4ec;
    --ink: #333333;
  }
  * { margin: 0; padding: 0; box-sizing: border-box; }
  html, body { width: 1200px; height: 861px; overflow: hidden; }
  body {
    background: var(--backdrop);
    font-family: "Jost", "Futura", sans-serif;
    position: relative;
  }
  .card {
    position: absolute;
    width: 525px;
    height: 300px;
    background: var(--card);
    overflow: hidden;
    box-shadow: 0 6px 18px rgba(0,0,0,0.18);
  }
  .card--front { left: 50px; top: 280px; }
  .card--back { left: 625px; top: 280px; }
  .card__bands { position: absolute; inset: 0; width: 100%; height: 100%; }
  .brand-name {
    position: absolute;
    font-weight: 300;
    color: var(--blue);
    letter-spacing: 4px;
    line-height: 1;
  }
  .card--front .brand-name { left: 150px; top: 125px; font-size: 62px; }
  .card--front .web { position: absolute; left: 170px; top: 200px; font-size: 22px; color: var(--ink); letter-spacing: 1px; }
  .card--back .brand-name { left: 40px; top: 42px; font-size: 50px; }
  .person { position: absolute; right: 40px; top: 60px; text-align: right; }
  .person__name { font-weight: 600; font-size: 24px; color: var(--pink); }
  .person__role { font-size: 15px; color: var(--ink); }
  .contacts { position: absolute; left: 30px; top: 150px; list-style: none; font-size: 15px; color: var(--ink); }
  .contacts li { display: flex; gap: 12px; line-height: 22px; }
  .contacts .label { width: 12px; font-weight: 600; color: var(--blue); }
</style>
</head>
<body>
  <section class="card card--front">
    <svg class="card__bands" viewBox="0 0 525 300" preserveAspectRatio="none" aria-hidden="true">
      <polygon points="0,0 380,0 0,170" fill="var(--plum)"/>
      <polygon points="0,40 300,0 380,0 0,200" fill="var(--pink)"/>
      <polygon points="0,170 380,0 420,0 0,195" fill="var(--pink-light)" opacity="0.85"/>
      <polygon points="0,0 200,0 0,90" fill="#3a0a20" opacity="0.6"/>
    </svg>
    <div class="brand-name">JH PROMO</div>
    <div class="web">www.jh-promo.com.au</div>
  </section>

  <section class="card card--back">
    <svg class="card__bands" viewBox="0 0 525 300" preserveAspectRatio="none" aria-hidden="true">
      <polygon points="525,95 525,300 170,300" fill="var(--blue-light)"/>
      <polygon points="525,115 525,300 230,300" fill="var(--blue)"/>
      <polygon points="525,150 525,300 300,300" fill="var(--blue-dark)"/>
      <polygon points="525,95 420,300 525,300" fill="var(--blue-dark)" opacity="0.6"/>
    </svg>
    <div class="brand-name">JH PROMO</div>
    <div class="person">
      <div class="person__name">Name Surname</div>
      <div class="person__role">Position</div>
    </div>
    <ul class="contacts">
      <li><span class="label">P</span>0461528390</li>
      <li><span class="label">E</span>sales@jh-promo.com.au</li>
      <li><span class="label">W</span>www.jh-promo.com.au</li>
    </ul>
  </section>
</body>
</html>
```